Event flyer for Sunday night Youth Group

Need a 4 x 6 or 5 x 7 flyer for a new youth group starting on April 14. The youth group is for students in middle school and high school so it needs to look fun and cool, but not childish. I prefer it not to include pictures of people unless it's so obscure you can't really see their faces. I've uploaded some pictures of flyers I like. I've also attached a couple versions of our logo to use on the flyer.
Information the flyer needs to include:
Youth Group
Sundays, 6-8pm (beginning April 14)
Location: Merriwick's - 4219 Hollowfern Ln S, Keizer, 97418
There will be dinner, games, friends, and a message.
Target Market(s)
Youth ages 13-18
Industry/Entity Type
Church
Colors
Designer to choose colors to be used in the design.
Look and feel

```html
<!DOCTYPE html>
<html lang="en">
<head>
<meta charset="utf-8">
<title>Youth Group — Sunday Nights</title>
<link rel="stylesheet" href="https://fonts.googleapis.com/css2?family=Cookie&family=Cormorant+Garamond:wght@400&family=Arimo:wght@400;700&display=swap">
<style>
  :root {
    --backdrop: #404042;
    --flyer-top: #0a1213;
    --flyer-mid: #132321;
    --flyer-deep: #060a0a;
    --sage: #8e9b8a;
    --sage-light: #a9b4a4;
    --sage-dark: #5f6d5d;
    --crowd-teal: #1d3a36;
    --white: #ffffff;
    --rule: #8c9694;
    --label-bg: #d4d4d4;
    --label-text: #3a3a3a;
  }
  html, body {
    margin: 0;
    width: 1200px;
    height: 1200px;
    overflow: hidden;
    background: var(--backdrop);
  }
  .flyer {
    position: absolute;
    left: 210px;
    top: 54px;
    width: 780px;
    height: 1092px;
    overflow: hidden;
    background: radial-gradient(ellipse at 50% 40%, var(--flyer-mid) 0%, var(--flyer-top) 55%, var(--flyer-deep) 100%);
    box-shadow: 0 18px 40px rgba(0,0,0,0.45);
    font-family: 'Arimo', Arial, sans-serif;
    color: var(--white);
  }
  .crowd-art {
    position: absolute;
    left: 0;
    bottom: 0;
    width: 780px;
    height: 560px;
    background: radial-gradient(ellipse at 60% 30%, rgba(38,74,68,0.55) 0%, rgba(20,40,37,0.45) 45%, rgba(6,10,10,0) 80%),
                linear-gradient(180deg, rgba(6,10,10,0) 0%, var(--crowd-teal) 55%, var(--flyer-deep) 100%);
    opacity: 0.85;
  }
  .brand {
    position: absolute;
    top: 52px;
    left: 0;
    width: 100%;
    text-align: center;
  }
  .brand-mark {
    display: block;
    width: 22px;
    height: 22px;
    margin: 0 auto 10px;
    background: var(--white);
  }
  .brand-name {
    font-size: 15px;
    font-weight: 400;
    letter-spacing: 2px;
    color: var(--white);
  }
  .brush-circle {
    position: absolute;
    left: 180px;
    top: 170px;
  }
  .title-youth {
    position: absolute;
    left: 40px;
    top: 150px;
    width: 700px;
    text-align: center;
    font-family: 'Cookie', cursive;
    font-size: 330px;
    line-height: 1;
    color: var(--white);
    text-shadow: 4px 5px 0 rgba(70,80,70,0.55);
  }
  .title-group {
    position: absolute;
    left: 388px;
    top: 410px;
    font-family: 'Cormorant Garamond', serif;
    font-size: 84px;
    color: var(--white);
    text-shadow: 3px 3px 0 rgba(60,70,60,0.6);
  }
  .details {
    position: absolute;
    top: 640px;
    left: 0;
    width: 100%;
    text-align: center;
  }
  .rule {
    width: 500px;
    height: 1px;
    margin: 0 auto;
    background: var(--rule);
  }
  .schedule {
    font-size: 46px;
    font-weight: 700;
    letter-spacing: 1px;
    margin: 12px 0 10px;
  }
  .start-date {
    font-size: 30px;
    font-weight: 700;
    letter-spacing: 1px;
    margin: 12px 0 24px;
  }
  .venue {
    display: inline-block;
    background: var(--label-bg);
    color: var(--label-text);
    font-size: 24px;
    padding: 8px 22px;
  }
  .offerings {
    margin-top: 38px;
    font-size: 24px;
    font-weight: 700;
    letter-spacing: 1.5px;
  }
</style>
</head>
<body>
  <main class="flyer">
    <div class="crowd-art" role="img" aria-label="Faint silhouettes of a cheering crowd with raised hands under soft teal bokeh lights"></div>

    <header class="brand">
      <span class="brand-mark"></span>
      <span class="brand-name">WAYPOINT FELLOWSHIP</span>
    </header>

    <svg class="brush-circle" width="440" height="360" viewBox="0 0 440 360" role="img" aria-label="Sage green brush-stroke circle behind the title">
      <ellipse cx="220" cy="180" rx="214" ry="174" fill="var(--sage-dark)" opacity="0.7"/>
      <ellipse cx="220" cy="180" rx="200" ry="162" fill="var(--sage)"/>
      <ellipse cx="200" cy="140" rx="150" ry="100" fill="var(--sage-light)" opacity="0.45"/>
    </svg>

    <div class="title-youth">Youth</div>
    <div class="title-group">Group</div>

    <section class="details">
      <div class="rule"></div>
      <div class="schedule">SUNDAYS, 6:00 - 8:00PM</div>
      <div class="rule"></div>
      <div class="start-date">Beginning April 14</div>
      <div class="venue">Merriwick's - 4219 Hollowfern Ln S, Keizer, 97418</div>
      <div class="offerings">DINNER • GAMES • FRIENDS • A MESSAGE</div>
    </section>
  </main>
</body>
</html>
```